Wedding Invitation for a wedding at home - personal, romantic event

Want a wedding invitation that is to be printed onto card.
Size to be 148mm x 210mm
For it to open like a book not tent card
Have a picture of a house that I want to be the front cover.
I've attached 2 pictures. I like the picture without the man but with the grass
For the photo to become a drawing and the colours to be brighter.
If you could use the picture of us and get us in one of the windows.
If you could put the picture of the dog maybe somewhere on the grass.
Love the colour of the sky in the picture of the beach

Words to be on the inside of the card:
Together with our families
You are invited to the Wedding Reception of Tessa Wynford and Owen Pashley
On Saturday 9th of September 2017 at 6pm
At Pashley's Keep, 41b, Morrow Crescent, Camberley, Surrey, GU19 6QT
Carriages at 1am
RSVP by Friday 27th of July to 07700 915 268

Words on the Back page:
With all that we have, we've been truly blessed.
Your presence and prayers are all that we request.
But if you desire to give nonetheless,
Monetary gift is one we suggest.

If the pages can be white.
Writing in gold
gold border on all pages

Target Market(s)

Wedding guests

Industry/Entity Type

Wedding

Font styles to use
Script

Requirements
Must have
• Romantic feel. Our wedding colours are white, gold and rose gold.
• Designer to be creative and I do not have much inspiration.
Nice to have
• metallic colours
• Maybe have MR & MRS in gold metallic on the front page

```html
<!DOCTYPE html>
<html lang="en">
<head>
<meta charset="utf-8">
<title>Wedding Invitation – Tessa &amp; Owen</title>
<link rel="stylesheet" href="https://fonts.googleapis.com/css2?family=Great+Vibes&family=Cinzel:wght@400&family=Lato:ital,wght@0,300;0,400;1,400&display=swap">
<style>
  :root {
    --backdrop: #efebe5;
    --paper: #ffffff;
    --gold: #c9a43c;
    --gold-light: #e8cf7a;
    --gold-deep: #a47e22;
    --rose: #f7d3dc;
    --sky-lilac: #d6d1ee;
    --sky-peach: #f6c99a;
    --sky-butter: #fbe6a6;
    --sky-blue: #b9cbe6;
    --brick: #c0704e;
    --brick-soft: #d9a48a;
  }
  * { box-sizing: border-box; margin: 0; padding: 0; }
  html, body { width: 1200px; height: 1200px; overflow: hidden; }
  body {
    background: var(--backdrop);
    font-family: "Lato", sans-serif;
    color: var(--gold);
  }
  .canvas {
    width: 1200px;
    height: 1200px;
    display: flex;
    flex-direction: column;
    align-items: center;
    justify-content: center;
    gap: 32px;
  }
  .spread {
    display: flex;
    box-shadow: 0 6px 18px rgba(90, 70, 40, 0.18);
  }
  .page {
    position: relative;
    width: 370px;
    height: 524px;
    background: var(--paper);
    overflow: hidden;
  }
  .page + .page { border-left: 1px solid #ece7dc; }
  .gold-frame {
    position: absolute;
    inset: 12px;
    border: 3px solid var(--gold);
    pointer-events: none;
    z-index: 3;
  }
  .gold-text {
    background: linear-gradient(180deg, var(--gold-light) 0%, var(--gold) 45%, var(--gold-deep) 100%);
    -webkit-background-clip: text;
    background-clip: text;
    color: transparent;
  }

  /* Back page */
  .back-page .verse {
    position: absolute;
    left: 0; right: 0; bottom: 46px;
    text-align: center;
    font-size: 10.5px;
    font-style: italic;
    line-height: 1.55;
    color: var(--gold);
  }

  /* Front cover */
  .cover-art {
    position: absolute;
    inset: 15px;
    background:
      radial-gradient(ellipse 62% 36% at 50% 56%, var(--brick) 0%, var(--brick-soft) 55%, rgba(217, 164, 138, 0) 100%),
      linear-gradient(180deg, var(--sky-lilac) 0%, var(--sky-butter) 18%, var(--sky-blue) 34%, #e9e4da 70%, #d8c2ae 100%);
  }
  .cover-names {
    position: absolute;
    top: 34px; left: 0; right: 0;
    text-align: center;
    font-family: "Great Vibes", cursive;
    font-weight: 400;
    font-size: 56px;
    line-height: 1;
    z-index: 2;
  }
  .cover-band {
    position: absolute;
    left: 15px; right: 15px; bottom: 40px;
    height: 92px;
    background: var(--rose);
    opacity: 0.94;
    z-index: 2;
    text-align: center;
    padding-top: 12px;
  }
  .cover-band .request {
    font-size: 12.5px;
    color: var(--gold-deep);
  }
  .cover-band .occasion {
    font-family: "Cinzel", serif;
    font-size: 32px;
    margin-top: 6px;
    color: var(--gold);
  }

  /* Inside left */
  .sky-art {
    position: absolute;
    inset: 15px;
    background: linear-gradient(180deg, var(--sky-lilac) 0%, #f4d3b0 18%, var(--sky-butter) 32%, var(--sky-peach) 45%, var(--sky-blue) 58%, #f3d2b2 72%, var(--sky-blue) 86%, #c6d3ea 100%);
  }

  /* Inside right */
  .invite-text {
    position: absolute;
    inset: 68px 22px 0;
    text-align: center;
  }
  .invite-text .intro {
    font-size: 13.5px;
    line-height: 1.6;
  }
  .invite-text .couple {
    font-family: "Cinzel", serif;
    font-size: 31px;
    line-height: 1.1;
    margin-top: 30px;
  }
  .invite-text .joiner {
    font-family: "Cinzel", serif;
    font-size: 19px;
    margin: 16px 0;
  }
  .invite-text .details {
    margin-top: 34px;
    font-size: 11.5px;
    line-height: 1.7;
  }
</style>
</head>
<body>
<main class="canvas">

  <section class="spread spread-outside">
    <article class="page back-page">
      <div class="gold-frame"></div>
      <p class="verse">
        With all that we have, we've been truly blessed.<br>
        Your presence and prayers are all that we request.<br>
        But if you desire to give nonetheless,<br>
        Monetary gift is one we suggest.
      </p>
    </article>

    <article class="page front-cover">
      <div class="cover-art" role="img" aria-label="Bright painted illustration of the couple's red-brick house under a pastel sunset sky, with the couple in a window and their dog on the lawn"></div>
      <h1 class="cover-names gold-text">Tessa &amp; Owen</h1>
      <div class="cover-band">
        <p class="request">Request the pleasure of your company to celebrate their</p>
        <p class="occasion">WEDDING</p>
      </div>
      <div class="gold-frame"></div>
    </article>
  </section>

  <section class="spread spread-inside">
    <article class="page inside-left">
      <div class="sky-art" role="img" aria-label="Pastel sunset sky photograph in lilac, peach and butter yellow"></div>
      <div class="gold-frame"></div>
    </article>

    <article class="page inside-right">
      <div class="gold-frame"></div>
      <div class="invite-text">
        <p class="intro">Together with our families<br>You are invited to the Wedding Reception of</p>
        <p class="couple gold-text">Tessa Wynford</p>
        <p class="joiner">AND</p>
        <p class="couple gold-text">Owen Pashley</p>
        <p class="details">
          On Saturday 9th of September 2017 at 6pm<br>
          At Pashley's Keep, 41b, Morrow Crescent, Camberley, Surrey<br>
          GU19 6QT<br>
          Carriages at 1am<br>
          RSVP by Friday 27th of July to 07700 915 268
        </p>
      </div>
    </article>
  </section>

</main>
</body>
</html>
```